Tri-fold Brochure Design for Banking Business

The brochure we have needs to be improved - more business like and more attractive. Logo file and brochure is attached. I would like to be able to edit the text after you get done. Your ideas and changes to text are welcome. See our website www.korvanbridgegrp.com for our theme. We can use indesign to edit the text after you complete. However, please make changes to the text we have in the design that it uploaded. Your comments and changes are welcome.

Target Market(s)

Human Resources and learning & development staff at the global investment banks - Pellham Trask, QWNR, etc.

Industry/Entity Type

Investment Banking

Logo Text

Korvan Bridge Group

Font styles to use
Serif
Sans Serif

Colors
33a6d7
0493ce
3277b5
fbf289
fdf9cf
fbee3e
0555a3
85acd3

Requirements
Must have
• Must be similar to our website www.korvanbridgegrp.com. Needs to be business-like, clean fonts, sharp design. Our logo - of course.
Nice to have
• City images - seems to be our theme.

```html
<!DOCTYPE html>
<html lang="en">
<head>
<meta charset="utf-8">
<title>Korvan Bridge Group – Tri-fold Brochure</title>
<link rel="stylesheet" href="https://fonts.googleapis.com/css2?family=Cardo:ital,wght@0,400;0,700;1,400&display=swap">
<style>
  :root {
    --stage: #34342f;
    --navy: #0e2a5c;
    --navy-deep: #0a1d45;
    --blue: #0555a3;
    --blue-mid: #3277b5;
    --blue-light: #33a6d7;
    --blue-soft: #85acd3;
    --yellow: #fbee3e;
    --white: #ffffff;
    --paper: #f4f6f9;
    --ink: #1d3a6e;
    --serif: "Cardo", Georgia, serif;
  }
  * { box-sizing: border-box; margin: 0; padding: 0; }
  html, body { width: 1010px; height: 1200px; overflow: hidden; }
  body { background: var(--stage); font-family: var(--serif); color: var(--white); position: relative; }

  .spread { position: absolute; left: 25px; width: 960px; height: 560px; box-shadow: 0 10px 30px rgba(0,0,0,.45); }
  .spread--outside { top: 30px; }
  .spread--inside { top: 610px; }
  .spread__art { position: absolute; inset: 0; width: 960px; height: 560px; display: block; }

  .panel { position: absolute; top: 0; width: 320px; height: 560px; padding: 44px 32px; }
  .panel--left { left: 0; }
  .panel--middle { left: 320px; }
  .panel--right { left: 640px; }

  .panel__title { font-size: 21px; font-weight: 700; letter-spacing: 1.5px; text-transform: uppercase; margin-bottom: 16px; }
  .body-copy { font-size: 11.5px; line-height: 1.55; margin-bottom: 10px; text-align: justify; }

  /* About */
  .about { padding-top: 150px; }

  /* Contact */
  .contact .panel__title { font-size: 15px; text-align: center; margin-bottom: 22px; }
  .region { border-left: 2px solid var(--white); padding-left: 8px; margin-bottom: 12px; }
  .region__name { font-size: 11px; font-weight: 700; letter-spacing: 1px; text-transform: uppercase; }
  .region__mail { font-size: 10px; opacity: .85; }
  .contact__tagline { text-align: center; margin-top: 18px; font-size: 19px; font-weight: 700; line-height: 1; }
  .contact__tagline span { display: block; color: var(--yellow); font-size: 15px; font-weight: 400; margin-top: 2px; }
  .contact__mark { width: 70px; height: 70px; margin: 26px auto 0; border: 3px solid var(--yellow); background: var(--blue); }
  .contact__details { position: absolute; left: 32px; right: 32px; bottom: 40px; text-align: center; }
  .contact__phone { font-size: 16px; font-weight: 700; margin-bottom: 4px; }
  .contact__small { font-size: 9.5px; opacity: .85; line-height: 1.4; }

  /* Brand name */
  .brand { display: flex; align-items: center; gap: 8px; }
  .brand__square { width: 12px; height: 12px; background: var(--yellow); flex: none; }
  .brand__name { font-family: var(--serif); font-weight: 700; font-size: 16px; color: var(--white); letter-spacing: 1px; text-transform: uppercase; white-space: nowrap; }

  /* Cover */
  .cover .brand { justify-content: center; margin-top: 4px; }
  .cover__headline { margin-top: 150px; text-align: center; line-height: 1; }
  .cover__line { display: block; font-size: 33px; }
  .cover__line--accent { color: var(--yellow); font-size: 42px; font-weight: 700; margin: 4px 0; }
  .cover__line--small { font-size: 26px; }

  /* Inside */
  .why .panel__title { font-size: 17px; }
  .why__list { list-style: none; margin-top: 10px; }
  .why__item { position: relative; padding-left: 16px; font-size: 11.5px; line-height: 1.45; margin-bottom: 7px; }
  .why__item::before { content: ""; position: absolute; left: 0; top: 5px; width: 7px; height: 7px; background: var(--white); }

  .services { padding-top: 100px; color: var(--ink); }
  .services .panel__title { color: var(--blue); font-size: 17px; text-align: center; }
  .services .body-copy { font-size: 11px; }

  .team { padding-top: 150px; }
  .team .panel__title { text-align: center; }
  .team__cta { margin-top: 26px; font-size: 19px; }
  .team__cta strong { display: block; color: var(--yellow); font-size: 27px; font-weight: 700; margin-top: 2px; }
</style>
</head>
<body>

<!-- OUTSIDE SPREAD -->
<section class="spread spread--outside">
  <svg class="spread__art" viewBox="0 0 960 560">
    <defs>
      <linearGradient id="navyFade" x1="0" y1="0" x2="0" y2="1">
        <stop offset="0" stop-color="#163b78"/>
        <stop offset="1" stop-color="#0a1d45"/>
      </linearGradient>
      <linearGradient id="cityFade" x1="0" y1="0" x2="0" y2="1">
        <stop offset="0" stop-color="#1d4a8a" stop-opacity="0"/>
        <stop offset="1" stop-color="#2a5c9c" stop-opacity=".55"/>
      </linearGradient>
      <linearGradient id="coverArt" x1="0" y1="0" x2="1" y2="1">
        <stop offset="0" stop-color="#33a6d7"/>
        <stop offset=".5" stop-color="#0555a3"/>
        <stop offset="1" stop-color="#fbee3e"/>
      </linearGradient>
    </defs>
    <rect width="960" height="560" fill="url(#navyFade)"/>
    <rect x="330" y="60" width="300" height="150" fill="#2a5c9c" opacity=".35" role="img" aria-label="Faint world map behind the regional contacts"/>
    <rect x="640" y="230" width="320" height="200" fill="url(#cityFade)" role="img" aria-label="City skyline photograph fading into the cover"/>
    <rect x="640" y="430" width="320" height="130" fill="url(#coverArt)" role="img" aria-label="Geometric shard artwork in light blue, blue and yellow"/>
    <line x1="320" y1="0" x2="320" y2="560" stroke="#000" stroke-opacity=".2"/>
    <line x1="640" y1="0" x2="640" y2="560" stroke="#000" stroke-opacity=".2"/>
  </svg>

  <article class="panel panel--left about">
    <h2 class="panel__title">About Us</h2>
    <p class="body-copy">Korvan Bridge Group is an efficient, dynamic training and consulting firm serving the world's leading financial institutions.</p>
    <p class="body-copy">Our globally based trainers have extensive experience, both as industry professionals and as educators.</p>
    <p class="body-copy">Our highly qualified team complements our training services, providing reliable and efficient support.</p>
  </article>

  <article class="panel panel--middle contact">
    <h2 class="panel__title">Get in Touch</h2>
    <div class="region"><p class="region__name">Global</p><p class="region__mail">info@korvanbridgegrp.com</p></div>
    <div class="region"><p class="region__name">Asia</p><p class="region__mail">asia@korvanbridgegrp.com</p></div>
    <div class="region"><p class="region__name">United States</p><p class="region__mail">us@korvanbridgegrp.com</p></div>
    <div class="region"><p class="region__name">Europe</p><p class="region__mail">europe@korvanbridgegrp.com</p></div>
    <p class="contact__tagline">Worldwide<span>Training Service</span></p>
    <div class="contact__mark"></div>
    <div class="contact__details">
      <p class="contact__phone">555 0147 2380</p>
      <p class="contact__small">info@korvanbridgegrp.com | www.korvanbridgegrp.com</p>
      <p class="contact__small">Unit 18D, Harlow Court, 42 Meridian Rd, Eastport City</p>
    </div>
  </article>

  <article class="panel panel--right cover">
    <div class="brand"><span class="brand__square"></span><span class="brand__name">Korvan Bridge Group</span></div>
    <h1 class="cover__headline">
      <span class="cover__line">Your Expert</span>
      <span class="cover__line cover__line--accent">Training &amp;</span>
      <span class="cover__line cover__line--small">Consulting Partner</span>
    </h1>
  </article>
</section>

<!-- INSIDE SPREAD -->
<section class="spread spread--inside">
  <svg class="spread__art" viewBox="0 0 960 560">
    <defs>
      <linearGradient id="paperCity" x1="0" y1="0" x2="0" y2="1">
        <stop offset="0" stop-color="#f4f6f9" stop-opacity="0"/>
        <stop offset="1" stop-color="#b9c4d4"/>
      </linearGradient>
      <linearGradient id="wedgeArt" x1="0" y1="0" x2="1" y2="1">
        <stop offset="0" stop-color="#0555a3"/>
        <stop offset="1" stop-color="#fbee3e"/>
      </linearGradient>
      <linearGradient id="topArt" x1="0" y1="0" x2="0" y2="1">
        <stop offset="0" stop-color="#3277b5"/>
        <stop offset="1" stop-color="#0e2a5c"/>
      </linearGradient>
    </defs>
    <rect width="320" height="560" fill="#0e2a5c"/>
    <rect x="0" y="330" width="320" height="230" fill="url(#wedgeArt)" role="img" aria-label="Geometric shard artwork in blue and yellow"/>
    <rect x="320" width="320" height="560" fill="#f4f6f9"/>
    <rect x="320" y="0" width="320" height="14" fill="#0555a3"/>
    <rect x="320" y="380" width="320" height="180" fill="url(#paperCity)" role="img" aria-label="Light city skyline photograph at the foot of the services panel"/>
    <rect x="640" width="320" height="560" fill="#0e2a5c"/>
    <rect x="640" y="0" width="320" height="130" fill="url(#topArt)" role="img" aria-label="Geometric shard artwork in blue tones"/>
    <line x1="320" y1="0" x2="320" y2="560" stroke="#000" stroke-opacity=".2"/>
    <line x1="640" y1="0" x2="640" y2="560" stroke="#000" stroke-opacity=".2"/>
  </svg>

  <article class="panel panel--left why">
    <h2 class="panel__title">Why Choose Us</h2>
    <p class="body-copy">We deliver practical, tailored training with measurable results for every client.</p>
    <ul class="why__list">
      <li class="why__item">Highly skilled trainers with banking expertise</li>
      <li class="why__item">Flexible, customised programme design</li>
      <li class="why__item">Strong client relationship management</li>
      <li class="why__item">Competitive pricing and flexibility</li>
      <li class="why__item">Outcome-driven approach aligned to your goals</li>
    </ul>
  </article>

  <article class="panel panel--middle services">
    <h2 class="panel__title">Our Services</h2>
    <p class="body-copy">Korvan Bridge Group provides best-in-class services for all our clients.</p>
    <p class="body-copy">We provide highly customised programs tailored to your specific requirements.</p>
    <p class="body-copy">Direct interaction between our clients, consulting trainers and client service staff ensures measurable outcomes.</p>
    <p class="body-copy">We facilitate learning outcomes using a blended method combining interactive workshops, case studies and a modern learning platform.</p>
    <p class="body-copy">Our materials are continuously updated to ensure accuracy and relevance of our services.</p>
  </article>

  <article class="panel panel--right team">
    <h2 class="panel__title">Our Team</h2>
    <p class="body-copy">Our consulting trainers are located globally and recognised by the industry as highly effective trainers and facilitators.</p>
    <p class="body-copy">Korvan Bridge Group provides global expertise for our programs with local talent for delivery.</p>
    <p class="team__cta">Need more information?<strong>Contact us!</strong></p>
  </article>
</section>

</body>
</html>
```